business card with logo Velmora Nails & Spa 2816 SW Quillan Ave Portland OR 97384

Would like to have a business card with our logo.
like bottle of polish with our logo or letter V on it
want something that first glance would let you know that it is a nail salon.
like the hands with polish bottle dripping.
like black or White back ground

Velmora Nails & Spa
(The Velvet Retreat)
2816 SW Quillan Ave
Portland, OR 97384
Call or Text: 1-503-555-0148
www.VelmoraNailsnSpa.example
Open 7 days a week.
After 7:00 PM is by appointment only.
Closed only on Thanksgiving & Christmas.

Target Market(s)

20%Man and 80%Woman 13-70

Industry/Entity Type

Business

Contact Information for Business Card

Elegant with Logo-Business name- address-phone-open days. closed day.

Font styles to use
Decorative
Script

Colors
000000

Requirements
Must have
• Logo and place for Technician Name
• Velmora Nails & Spa
• (The Velvet Retreat)
• 2816 SW Quillan Ave
• Portland, OR 97384
• Call or Text: 1-503-555-0148
• Open 7 days a week
• Closed only on Thanksgiving & Christmas.
• We accepted all major credit cards but prefer cash. Thank you
Nice to have
• Nail polish bottle with our Logo or letter V
Should not have
• too colorful

```html
<!DOCTYPE html>
<html lang="en">
<head>
<meta charset="utf-8">
<title>Velmora Nails &amp; Spa — Business Card</title>
<link rel="stylesheet" href="https://fonts.googleapis.com/css2?family=Source+Sans+3:ital,wght@0,400;0,600;0,700;1,400;1,600&family=Yesteryear&display=swap">
<style>
  :root {
    --backdrop: #161616;
    --card-white: #ffffff;
    --lime: #b5d334;
    --ink: #111111;
    --accent-red: #e0261f;
    --art-grey: #d9d9d9;
  }
  * { margin: 0; padding: 0; box-sizing: border-box; }
  html, body {
    width: 1200px; height: 900px; overflow: hidden;
    background: var(--backdrop);
  }
  .stage { position: relative; width: 1200px; height: 900px; }
  .card {
    position: absolute; top: 306px;
    width: 440px; height: 271px;
    border-radius: 10px; overflow: hidden;
    font-family: "Source Sans 3", Arial, sans-serif;
    color: var(--ink);
  }
  .card--front { left: 149px; background: var(--card-white); }
  .card--back { left: 608px; background: var(--lime); text-align: center; }

  .front-shapes { position: absolute; inset: 0; }

  .brand { position: absolute; color: var(--ink); font-weight: 600; line-height: 1; }
  .brand__name { display: block; }
  .brand__tag { display: block; }
  .card--front .brand { left: 26px; top: 40px; }
  .card--front .brand__name { font-size: 34px; }
  .card--front .brand__tag { font-size: 13px; margin-top: 4px; padding-left: 62px; }

  .contact {
    position: absolute; right: 22px; top: 104px;
    text-align: right; line-height: 1.3;
  }
  .contact__name {
    font-family: "Yesteryear", cursive;
    color: var(--accent-red); font-size: 17px; letter-spacing: 0.5px;
  }
  .contact__title { font-size: 12.5px; }
  .contact__phone { font-size: 13.5px; font-style: italic; font-weight: 600; margin-top: 11px; }
  .contact__business { font-size: 13px; font-weight: 700; margin-top: 13px; }
  .contact__subtitle { font-size: 12px; font-weight: 700; }
  .contact__address { font-size: 12.5px; }

  .card--back .brand { left: 0; right: 0; top: 54px; }
  .card--back .brand__name { font-size: 40px; }
  .card--back .brand__tag { font-size: 15px; margin-top: 4px; }

  .hours { position: absolute; left: 0; right: 0; top: 146px; line-height: 1.3; }
  .hours__line { font-size: 14.5px; }
  .hours__closed { font-size: 14px; font-style: italic; margin-top: 5px; }
  .hours__payment { font-size: 10.5px; text-transform: uppercase; margin-top: 8px; }
  .hours__web { font-size: 12.5px; margin-top: 7px; }
</style>
</head>
<body>
<main class="stage">
  <section class="card card--front">
    <svg class="front-shapes" width="440" height="271" viewBox="0 0 440 271">
      <path d="M410 0 H440 V271 H90 C180 200 250 120 300 60 C330 25 370 5 410 0 Z" fill="var(--lime)"/>
      <path role="img" aria-label="Line illustration of a slender leg and foot with red painted toenails, reaching up to a hand with red painted nails" d="M20 262 C120 250 200 160 250 90 C280 45 320 10 410 4 C395 30 360 45 330 60 C280 110 220 200 170 262 Z" fill="var(--art-grey)" opacity="0.55"/>
    </svg>
    <div class="brand">
      <span class="brand__name">Velmora</span>
      <span class="brand__tag">Nails n Spa</span>
    </div>
    <div class="contact">
      <p class="contact__name">Daniel Hartwell</p>
      <p class="contact__title">Managing Director</p>
      <p class="contact__phone">Call or Text: 1-503-555-0148</p>
      <p class="contact__business">VELMORA NAILS &amp; SPA</p>
      <p class="contact__subtitle">(The Velvet Retreat)</p>
      <p class="contact__address">2816 SW Quillan Ave</p>
      <p class="contact__address">Portland, OR 97384</p>
    </div>
  </section>

  <section class="card card--back">
    <div class="brand">
      <span class="brand__name">Velmora</span>
      <span class="brand__tag">Nails n Spa</span>
    </div>
    <div class="hours">
      <p class="hours__line">Open 7 days a week.</p>
      <p class="hours__line">After 7:00 PM is by appointment only.</p>
      <p class="hours__closed">Closed only on Thanksgiving &amp; Christmas.</p>
      <p class="hours__payment">We accepted all major credit cards but prefer cash. Thank you</p>
      <p class="hours__web">www.VelmoraNailsnSpa.example</p>
    </div>
  </section>
</main>
</body>
</html>
```